Small rum distillery looking for bottle design

Small rum distillery in Estonia. Looking for bottle lable design. It should be simple but at the same time point out from the variety of other bottles.
As we are a small nordic country, design can be some how nordic or represent our country. It can also have some connection with sailing or sea as we know it pirates love it.
Bottle we are using is Corvane 540

Industry/Entity Type

food and beverage

Other font styles liked:
• Baskerville

```html
<!DOCTYPE html>
<html lang="en">
<head>
<meta charset="utf-8">
<title>Halvik Distillery – Original Blend Label</title>
<link rel="stylesheet" href="https://fonts.googleapis.com/css2?family=Libre+Baskerville:wght@400;700&family=Cinzel:wght@700&display=swap">
<style>
  :root {
    --backdrop: #1b1530;
    --label-black: #141414;
    --gold: #c9a96b;
    --gold-light: #e6cf9a;
    --gold-dark: #8f7445;
    --red: #c8201e;
    --white: #f4f2ee;
  }
  html, body {
    margin: 0;
    padding: 0;
    width: 1129px;
    height: 1200px;
    overflow: hidden;
    background: var(--backdrop);
  }
  .label-canvas {
    display: block;
    width: 1129px;
    height: 1200px;
  }
  .brand-name {
    font-family: "Libre Baskerville", serif;
    font-size: 76px;
    fill: var(--gold);
    letter-spacing: 2px;
  }
  .brand-sub {
    font-family: "Libre Baskerville", serif;
    font-size: 24px;
    fill: var(--gold);
    letter-spacing: 9px;
  }
  .blend-title {
    font-family: "Cinzel", serif;
    font-weight: 700;
    font-size: 62px;
    fill: var(--white);
    letter-spacing: 1px;
  }
  .age-word {
    font-family: "Libre Baskerville", serif;
    font-weight: 700;
    font-size: 23px;
    fill: var(--white);
    letter-spacing: 1px;
  }
  .age-number {
    font-family: "Libre Baskerville", serif;
    font-weight: 700;
    font-size: 50px;
    fill: var(--gold);
  }
  .style-tag {
    font-family: "Libre Baskerville", serif;
    font-weight: 700;
    font-size: 19px;
    fill: var(--label-black);
    letter-spacing: 4px;
  }
  .volume {
    font-family: "Libre Baskerville", serif;
    font-weight: 700;
    font-size: 30px;
    fill: var(--white);
  }
  .volume-unit { font-size: 21px; }
</style>
</head>
<body>
<svg class="label-canvas" viewBox="0 0 1129 1200" xmlns="http://www.w3.org/2000/svg">
  <defs>
    <linearGradient id="band-left" x1="0" x2="1">
      <stop offset="0" stop-color="#c8201e" stop-opacity="0"/>
      <stop offset="0.55" stop-color="#c8201e" stop-opacity="0.7"/>
      <stop offset="1" stop-color="#c8201e"/>
    </linearGradient>
    <linearGradient id="band-right" x1="1" x2="0">
      <stop offset="0" stop-color="#c8201e" stop-opacity="0"/>
      <stop offset="0.55" stop-color="#c8201e" stop-opacity="0.7"/>
      <stop offset="1" stop-color="#c8201e"/>
    </linearGradient>
    <linearGradient id="town-scene" x1="0" y1="0" x2="0" y2="1">
      <stop offset="0" stop-color="#8c8c8c"/>
      <stop offset="0.35" stop-color="#5e5e5e"/>
      <stop offset="1" stop-color="#2a2a2a"/>
    </linearGradient>
    <linearGradient id="tag-gold" x1="0" x2="1">
      <stop offset="0" stop-color="#8f7445"/>
      <stop offset="0.5" stop-color="#e6cf9a"/>
      <stop offset="1" stop-color="#8f7445"/>
    </linearGradient>
    <path id="blend-arc" d="M245 925 Q565 845 885 925"/>
  </defs>

  <!-- label body -->
  <path class="label-body" fill="var(--label-black)"
        d="M115 280 H388 V250 Q388 160 565 160 Q742 160 742 250 V280 H1015 V1095 H115 Z"/>

  <!-- frame -->
  <g class="label-frame" fill="none">
    <path stroke="var(--gold)" stroke-width="2"
          d="M135 312 H400 V252 Q400 175 565 175 Q730 175 730 252 V312 H995 V1068 H135 Z"/>
    <path stroke="var(--red)" stroke-width="2"
          d="M150 326 H412 V254 Q412 188 565 188 Q718 188 718 254 V326 H980 V1054 H150 Z"/>
    <g stroke="var(--gold)" stroke-width="2">
      <rect x="124" y="300" width="24" height="24"/>
      <rect x="982" y="300" width="24" height="24"/>
      <rect x="124" y="1056" width="24" height="24"/>
      <rect x="982" y="1056" width="24" height="24"/>
      <line x1="162" y1="340" x2="162" y2="1040"/>
      <line x1="968" y1="340" x2="968" y2="1040"/>
    </g>
  </g>

  <!-- red side bands -->
  <rect x="175" y="352" width="205" height="84" fill="url(#band-left)"/>
  <rect x="750" y="352" width="205" height="84" fill="url(#band-right)"/>

  <!-- brand -->
  <circle cx="565" cy="245" r="26" fill="var(--gold)"/>
  <text class="brand-name" x="565" y="410" text-anchor="middle">HALVIK</text>
  <line x1="395" y1="428" x2="735" y2="428" stroke="var(--gold)" stroke-width="2"/>
  <text class="brand-sub" x="565" y="466" text-anchor="middle">DISTILLERY</text>

  <!-- town view -->
  <rect x="240" y="495" width="650" height="318" fill="url(#town-scene)"
        role="img" aria-label="Black and white engraving-style view over Tallinn old town rooftops and church spire"/>

  <!-- product title -->
  <path d="M215 882 Q565 768 915 882" fill="none" stroke="var(--red)" stroke-width="3"/>
  <text class="blend-title" text-anchor="middle">
    <textPath href="#blend-arc" startOffset="50%">ORIGINAL BLEND</textPath>
  </text>
  <path d="M250 968 Q565 898 880 968" fill="none" stroke="var(--red)" stroke-width="3"/>

  <!-- age statement -->
  <g class="age-statement">
    <line x1="435" y1="968" x2="525" y2="968" stroke="var(--white)" stroke-width="1.5"/>
    <line x1="435" y1="1000" x2="525" y2="1000" stroke="var(--white)" stroke-width="1.5"/>
    <line x1="605" y1="968" x2="705" y2="968" stroke="var(--white)" stroke-width="1.5"/>
    <line x1="605" y1="1000" x2="705" y2="1000" stroke="var(--white)" stroke-width="1.5"/>
    <text class="age-word" x="480" y="993" text-anchor="middle">AGED</text>
    <text class="age-number" x="565" y="1003" text-anchor="middle">12</text>
    <text class="age-word" x="655" y="993" text-anchor="middle">YEARS</text>
  </g>

  <rect x="440" y="1014" width="250" height="34" fill="url(#tag-gold)"/>
  <text class="style-tag" x="567" y="1038" text-anchor="middle">ESTONIA RUM</text>

  <text class="volume" x="928" y="1040" text-anchor="end">750<tspan class="volume-unit">ML</tspan></text>
</svg>
</body>
</html>
```